Half-off Holiday Sale: Larkwood Academy

The online course called Larkwood Academy. Once a year, I run a 1/2 off special (expired Dec 31). You can see what the school is all about here: larkwood-academy.com and I'll attach a picture of the current ad we're running.
www.larkwood-academy.com

Please stick with the brain/puzzle logo as the theme, but make the 50% off appealing and inviting.

** I plan on paying for more than one design. I'd like to buy a few different ones!

Target Market(s)

People with Parkinson's disease and their families.

Industry/Entity Type

medical care/ education

Requirements
Must have
• LA School (Larkwood Academy) logo; Must say "50% off" or something like that.

```html
<!DOCTYPE html>
<html lang="en">
<head>
<meta charset="utf-8">
<title>Larkwood Academy – 50% Off</title>
<link rel="stylesheet" href="https://fonts.googleapis.com/css2?family=Exo+2:wght@700&family=Montserrat:wght@800&family=Arimo:wght@400&display=swap">
<style>
  :root {
    --backdrop: #444444;
    --paper-light: #f7f7f7;
    --paper-mid: #dcdddf;
    --navy: #1a2466;
    --navy-deep: #141c52;
    --orange: #e8501f;
    --slate: #8b8e90;
    --tagline: #6f7275;
    --white: #ffffff;
  }
  * { margin: 0; padding: 0; box-sizing: border-box; }
  html, body {
    width: 1200px;
    height: 1000px;
    overflow: hidden;
    background: var(--backdrop);
  }
  .ad-card {
    position: absolute;
    left: 165px;
    top: 65px;
    width: 870px;
    height: 870px;
    overflow: hidden;
    background: radial-gradient(ellipse at 50% 30%, var(--paper-light) 0%, var(--paper-mid) 100%);
  }
  .wave-art {
    position: absolute;
    inset: 0;
    width: 870px;
    height: 870px;
  }
  .brand-mark {
    position: absolute;
    left: 335px;
    top: 80px;
    width: 200px;
    height: 200px;
    border-radius: 50%;
    background: var(--orange);
  }
  .brand-name {
    position: absolute;
    left: 0;
    width: 870px;
    top: 308px;
    text-align: center;
    font-family: "Exo 2", sans-serif;
    font-weight: 700;
    font-size: 64px;
    letter-spacing: 1px;
    line-height: 1;
    color: var(--slate);
  }
  .brand-tagline {
    position: absolute;
    left: 0;
    width: 870px;
    top: 386px;
    text-align: center;
    font-family: "Arimo", sans-serif;
    font-size: 20px;
    color: var(--tagline);
  }
  .offer {
    position: absolute;
    left: 96px;
    top: 560px;
    display: flex;
    align-items: baseline;
    font-family: "Montserrat", sans-serif;
    font-weight: 800;
    line-height: 1;
  }
  .offer-amount {
    font-size: 232px;
    letter-spacing: -6px;
    color: var(--white);
  }
  .offer-label {
    font-size: 88px;
    color: var(--orange);
    margin-left: 4px;
  }
  .offer-rule {
    position: absolute;
    top: 819px;
    height: 6px;
  }
  .offer-rule--left { left: 45px; width: 292px; background: var(--orange); }
  .offer-rule--mid { left: 348px; width: 175px; background: var(--white); }
  .offer-rule--right { left: 535px; width: 292px; background: var(--orange); }
</style>
</head>
<body>
  <main class="ad-card">
    <svg class="wave-art" viewBox="0 0 870 870" aria-hidden="true">
      <path d="M0,412 C110,500 300,535 480,482 C640,438 780,432 870,478 L870,870 L0,870 Z" fill="var(--orange)"/>
      <path d="M0,455 C130,535 320,548 500,494 C650,452 790,452 870,486 L870,870 L0,870 Z" fill="var(--white)"/>
    </svg>
    <svg class="wave-art" viewBox="0 0 870 870" role="img" aria-label="Photo of a family relaxing together on a sofa, tinted navy blue">
      <defs>
        <linearGradient id="photoTint" x1="0" y1="0" x2="0" y2="1">
          <stop offset="0" stop-color="var(--navy)"/>
          <stop offset="1" stop-color="var(--navy-deep)"/>
        </linearGradient>
      </defs>
      <path d="M0,470 C140,545 330,556 510,502 C660,460 795,460 870,492 L870,870 L0,870 Z" fill="url(#photoTint)"/>
    </svg>

    <div class="brand-mark" aria-hidden="true"></div>
    <h1 class="brand-name">LARKWOOD ACADEMY</h1>
    <p class="brand-tagline">An Online Course for Patients and Providers</p>

    <p class="offer">
      <span class="offer-amount">50%</span><span class="offer-label">OFF</span>
    </p>
    <div class="offer-rule offer-rule--left"></div>
    <div class="offer-rule offer-rule--mid"></div>
    <div class="offer-rule offer-rule--right"></div>
  </main>
</body>
</html>
```